Property Management Company looking for a high-end business card, letterhead and envelope design.

We provide high-end / boutique property management for real estate investors or individuals looking for someone to manage their portfolio. we are looking for a cohesive high-end design for our business cards, letterhead and envelopes.

Target Market(s)

Real Estate Investors

Industry/Entity Type

Real Estate

Requirements
Must have
• business card, letterhead and envelope design - logo attached

```html
<!DOCTYPE html>
<html lang="en">
<head>
<meta charset="utf-8">
<title>Northgate Property Management – Stationery</title>
<link href="https://fonts.googleapis.com/css2?family=Montserrat:wght@500;600;700&family=Nunito+Sans:wght@400;600&display=swap" rel="stylesheet">
<style>
  :root {
    --navy: #17406f;
    --navy-deep: #0e3561;
    --navy-text: #1a2f5c;
    --backdrop: #ececec;
    --paper: #ffffff;
    --paper-shade: #e8e8e8;
    --window: #a3a3a3;
  }
  * { margin: 0; padding: 0; box-sizing: border-box; }
  html, body { width: 1200px; height: 1200px; overflow: hidden; }
  body {
    position: relative;
    background: var(--backdrop);
    font-family: "Nunito Sans", sans-serif;
    color: var(--navy-text);
  }
  .sheet { position: absolute; overflow: hidden; box-shadow: 0 2px 8px rgba(0,0,0,0.18); }

  .brand { position: absolute; display: flex; align-items: flex-start; gap: 6px;
    font-family: "Montserrat", sans-serif; font-weight: 600; color: var(--navy); line-height: 1; }
  .brand-mark { width: 8px; height: 8px; background: currentColor; margin-top: 4px; }
  .brand-name { display: block; letter-spacing: 0.14em; }
  .brand-sub { display: block; letter-spacing: 0.2em; margin-top: 4px; }

  /* Letterhead */
  .letterhead { left: 62px; top: 75px; width: 504px; height: 713px;
    background: linear-gradient(165deg, var(--paper-shade) 0%, var(--paper) 70%); }
  .letterhead .brand { left: 28px; top: 20px; }
  .letterhead .brand-name { font-size: 23px; }
  .letterhead .brand-sub { font-size: 9.5px; }
  .letter-subject { position: absolute; left: 72px; top: 120px;
    font-family: "Montserrat", sans-serif; font-weight: 600; font-size: 11.5px; letter-spacing: 0.02em; }
  .letter-body { position: absolute; left: 72px; top: 156px; width: 362px;
    font-size: 9.4px; line-height: 15.2px; }
  .letter-body p + p { margin-top: 15.2px; }
  .letter-closing { position: absolute; left: 300px; top: 553px; width: 120px; text-align: center; font-size: 9.5px; }
  .letter-signature { position: absolute; left: 290px; top: 603px; width: 140px; text-align: center;
    font-family: "Montserrat", sans-serif; }
  .signature-name { font-size: 11.5px; font-weight: 500; letter-spacing: 0.03em; }
  .signature-role { font-size: 7px; font-weight: 600; letter-spacing: 0.04em; }
  .signature-company { margin-top: 10px; font-size: 9.5px; font-weight: 600; line-height: 1.25; }
  .contact-block { position: absolute; font-size: 7px; line-height: 12px; }
  .letterhead .contact-block { left: 21px; top: 646px; }
  .contact-web { margin-top: 12px; }
  .accent-band { position: absolute; background: var(--navy); }
  .letterhead .accent-band { right: 0; bottom: 0; width: 110px; height: 10px; }

  /* Business cards */
  .card { width: 216px; height: 131px; top: 176px; }
  .card-front { left: 646px; background: var(--navy-deep); }
  .card-front .card-panel { position: absolute; right: 0; top: 0; width: 80px; height: 100%; background: #0f3158; }
  .card-front .brand { left: 16px; top: 56px; color: #c9ced6; }
  .card-front .brand-mark { width: 5px; height: 5px; margin-top: 2px; }
  .card-front .brand-name { font-size: 11.5px; }
  .card-front .brand-sub { font-size: 5px; margin-top: 2px; }
  .card-back { left: 890px; background: var(--paper); }
  .card-back .brand { left: 16px; top: 12px; }
  .card-back .brand-mark { width: 5px; height: 5px; margin-top: 2px; }
  .card-back .brand-name { font-size: 11.5px; }
  .card-back .brand-sub { font-size: 5px; margin-top: 2px; }
  .card-person { position: absolute; left: 99px; top: 46px; font-family: "Montserrat", sans-serif; color: var(--navy); }
  .card-person-name { font-size: 11px; font-weight: 600; letter-spacing: 0.02em; }
  .card-person-role { font-size: 4.5px; color: #555; letter-spacing: 0.06em; }
  .card-contact { position: absolute; left: 99px; top: 72px; font-size: 4.2px; line-height: 9.4px; }

  /* Envelopes */
  .envelope { left: 597px; width: 553px; height: 286px; }
  .envelope-back { top: 502px;
    background: linear-gradient(90deg, #e6e6e6 0%, #f6f6f6 60%, #eaeaea 100%); }
  .envelope-back svg { position: absolute; left: 0; top: 0; }
  .envelope-front { top: 827px;
    background: linear-gradient(160deg, #fafafa 0%, #ececec 100%); }
  .envelope-front .brand { left: 17px; top: 23px; }
  .envelope-front .brand-name { font-size: 18.5px; }
  .envelope-front .brand-sub { font-size: 8px; }
  .envelope-window { position: absolute; left: 262px; top: 140px; width: 243px; height: 108px;
    border-radius: 10px; background: linear-gradient(135deg, #9a9a9a 0%, #b4b4b4 50%, #8f8f8f 100%); }
  .envelope-front .contact-block { left: 24px; top: 218px; }
  .envelope-front .accent-band { right: 0; bottom: 0; width: 200px; height: 10px; }
</style>
</head>
<body>

<section class="sheet letterhead" aria-label="Letterhead">
  <div class="brand"><span class="brand-mark"></span><span><span class="brand-name">NORTHGATE</span><span class="brand-sub">PROPERTY MANAGEMENT</span></span></div>
  <h1 class="letter-subject">SUBJECT LETTER</h1>
  <div class="letter-body">
    <p>Lorem ipsum dolor sit amet, consectetur adipiscing elit. Mauris et tempor nunc. Quisque in quam sed libero tincidunt euismod ac sed nisi. Aliquam gravida vel odio sit amet blandit. Quisque blandit ex in commodo tempor. Cras at sem sapien. Mauris vel augue at sem auctor blandit in maximus ipsum. Quisque at ipsum sit amet justo suscipit placerat sit amet at mauris. Praesent eget leo eu arcu consequat consectetur. Nulla et consequat nunc. Curabitur sit amet urna mauris. Phasellus nec vestibulum odio. Suspendisse blandit orci sed ante feugiat feugiat.</p>
    <p>Vestibulum suscipit nulla vitae ullamcorper sollicitudin. Vestibulum finibus urna tortor. Aliquam erat volutpat. Sed ultrices ligula aliquam tortor dapibus hendrerit. Ut ut felis quam. Mauris mollis scelerisque turpis id interdum. Vivamus id mi nec dui tempor cursus ac tempor sapien. In sed diam sagittis, sodales mauris et, egestas felis. Nulla facilisi. Praesent id malesuada eros. Nulla euismod metus nec massa aliquet porttitor. Sed ornare quam orci, at ultrices elit egestas non.</p>
    <p>Sed facilisis enim at interdum vulputate. Proin tincidunt vitae dui nec congue. Nullam eleifend finibus suscipit. Duis nec libero id purus ultricies hendrerit. Cras ante velit, pretium vitae laoreet at, accumsan in lacus. Nunc eget ligula ac eros venenatis placerat ac vitae magna. Aliquam dictum massa tempus lorem malesuada, a vestibulum nisi aliquet. Vestibulum purus nibh, maximus a ante ac, convallis dictum velit. Nam vel sodales sem. Nam rutrum ipsum et ex commodo sollicitudin. Nullam mattis, mauris sit amet convallis eleifend, ligula augue tincidunt urna, vitae dapibus eros odio et lectus. Quisque ornare metus vitae nunc lobortis, id ultricies orci maximus.</p>
  </div>
  <p class="letter-closing">Best Regards,</p>
  <div class="letter-signature">
    <div class="signature-name">DANIEL REYES</div>
    <div class="signature-role">ACCOUNT MANAGER</div>
    <div class="signature-company">NORTHGATE<br>Property Management</div>
  </div>
  <div class="contact-block">
    <div>123 Dummy Road, Lorem Ipsum, Country</div>
    <div>+00 1234 5678 9012</div>
    <div class="contact-web">www.northgateproperty.com</div>
  </div>
  <div class="accent-band"></div>
</section>

<section class="sheet card card-front" aria-label="Business card front">
  <div class="card-panel"></div>
  <div class="brand"><span class="brand-mark"></span><span><span class="brand-name">NORTHGATE</span><span class="brand-sub">PROPERTY MANAGEMENT</span></span></div>
</section>

<section class="sheet card card-back" aria-label="Business card back">
  <div class="brand"><span class="brand-mark"></span><span><span class="brand-name">NORTHGATE</span><span class="brand-sub">PROPERTY MANAGEMENT</span></span></div>
  <div class="card-person">
    <div class="card-person-name">DANIEL REYES</div>
    <div class="card-person-role">ACCOUNT MANAGER</div>
  </div>
  <div class="card-contact">
    <div>123 Dummy Road, Lorem Ipsum, Country</div>
    <div>+00 1234 5678 9012</div>
    <div>contact@northgateproperty.com</div>
    <div>www.northgateproperty.com</div>
  </div>
</section>

<section class="sheet envelope envelope-back" aria-label="Envelope back">
  <svg width="553" height="286" viewBox="0 0 553 286">
    <path d="M0 0 H553 Q548 28 528 38 L296 144 Q276 153 256 144 L25 38 Q5 28 0 0 Z" fill="#114e86"/>
  </svg>
</section>

<section class="sheet envelope envelope-front" aria-label="Envelope front">
  <div class="brand"><span class="brand-mark"></span><span><span class="brand-name">NORTHGATE</span><span class="brand-sub">PROPERTY MANAGEMENT</span></span></div>
  <div class="envelope-window"></div>
  <div class="contact-block">
    <div>123 Dummy Road, Lorem Ipsum, Country</div>
    <div>+00 1234 5678 9012</div>
    <div class="contact-web">www.northgateproperty.com</div>
  </div>
  <div class="accent-band"></div>
</section>

</body>
</html>
```